Calendar design with baby pictures

I need to get 2 calendars designed, one wall hanging A5 size and one table top. I want to use my baby pics on it in very creative way. On some months i just want to use one picture and on some i will want to use a collage of few pics. The design should allow me to place pictures myself later on as i dont want to upload so many pics here.

```html
<!DOCTYPE html>
<html lang="en">
<head>
<meta charset="utf-8">
<title>Baby Photo Calendar – Autumn 2015</title>
<link rel="stylesheet" href="https://fonts.googleapis.com/css2?family=Alfa+Slab+One&family=Delius&display=swap">
<style>
  :root {
    --page-bg: #ffffff;
    --frame: #222222;
    --pill-bg: #ffffff;
    --day-ink: #222222;
    --weekend-ink: #e0157a;
    --out-ink: #b8b8b8;
    --sep-accent: #e2062c;
    --sep-soft: #f08a78;
    --oct-accent: #a87a8a;
    --oct-soft: #c9a9b4;
    --nov-accent: #7272b8;
    --nov-soft: #a0a0d4;
    --dec-accent: #b06fb8;
    --dec-soft: #cfa0d2;
  }
  * { margin: 0; padding: 0; box-sizing: border-box; }
  html, body { width: 1002px; height: 1200px; overflow: hidden; }
  body {
    position: relative;
    background: var(--page-bg);
    border: 1px solid var(--frame);
    font-family: "Delius", "Comic Sans MS", cursive;
  }
  .month-page {
    position: absolute;
    display: flex;
    flex-direction: column;
    background: var(--page-bg);
    box-shadow: 4px 4px 6px rgba(0,0,0,.55);
  }
  .month-page--sep { left: 146px; top: 18px;  width: 342px; height: 484px; --accent: var(--sep-accent); --soft: var(--sep-soft); }
  .month-page--oct { left: 525px; top: 18px;  width: 341px; height: 484px; --accent: var(--oct-accent); --soft: var(--oct-soft); }
  .month-page--nov { left: 142px; top: 520px; width: 348px; height: 496px; --accent: var(--nov-accent); --soft: var(--nov-soft); }
  .month-page--dec { left: 525px; top: 520px; width: 353px; height: 500px; --accent: var(--dec-accent); --soft: var(--dec-soft); }

  .month-title {
    height: 60px;
    flex: none;
    background: var(--accent);
    border-bottom: 3px dotted #ffffff;
    color: #ffffff;
    font-family: "Alfa Slab One", Georgia, serif;
    font-size: 24px;
    letter-spacing: .5px;
    text-align: right;
    padding: 24px 24px 0 0;
    line-height: 1;
  }
  .photo-slot { flex: none; height: 270px; }
  .month-page--nov .photo-slot { height: 276px; }
  .month-page--dec .photo-slot { height: 280px; }
  .photo-slot--sep { background: linear-gradient(160deg, #6e6a66 0%, #b9b3a8 45%, #8fbf8a 70%, #d04a4a 100%); }
  .photo-slot--nov { background: linear-gradient(180deg, #3f6a38 0%, #5b6fa8 35%, #c99a80 60%, #ece9e4 100%); }
  .photo-slot--dec { background: linear-gradient(120deg, #2c2a2a 0%, #6a3030 35%, #c8c2bc 60%, #d9a040 85%, #e9e6e2 100%); }

  .photo-collage {
    flex: none;
    height: 270px;
    display: grid;
    grid-template-columns: 187px 1fr;
    grid-template-rows: 97px 1fr;
    gap: 2px;
    background: #ffffff;
  }
  .photo-collage .tile--main { grid-row: 1 / 3; background: linear-gradient(170deg, #5a4a40 0%, #e8e0d0 45%, #3a3a8a 75%, #6a4a3a 100%); }
  .photo-collage .tile--top  { background: linear-gradient(160deg, #6a5a50 0%, #d8b8a0 55%, #f0f0f0 100%); }
  .photo-collage .tile--bottom { background: linear-gradient(170deg, #4a4040 0%, #cfa890 45%, #2e2e70 75%, #e8e8e8 100%); }

  .date-grid {
    flex: 1;
    background: linear-gradient(180deg, var(--soft) 0%, #ffffff 100%);
    display: grid;
    grid-template-columns: repeat(7, 34px);
    grid-auto-rows: 16px;
    column-gap: 8px;
    row-gap: 6px;
    justify-content: center;
    align-content: start;
    padding-top: 6px;
  }
  .weekday {
    background: var(--accent);
    color: #ffffff;
    border-radius: 50%;
    font-size: 12px;
    line-height: 16px;
    text-align: center;
  }
  .day {
    background: var(--pill-bg);
    color: var(--day-ink);
    border-radius: 50%;
    font-size: 12px;
    line-height: 16px;
    text-align: center;
    box-shadow: 0 1px 2px rgba(0,0,0,.25);
  }
  .day.weekend { color: var(--weekend-ink); }
  .day.outside { color: var(--out-ink); }
</style>
</head>
<body>

<section class="month-page month-page--sep">
  <h2 class="month-title">September 2015</h2>
  <div class="photo-slot photo-slot--sep" role="img" aria-label="Photo slot: smiling baby sitting on a grey sofa"></div>
  <div class="date-grid">
    <span class="weekday">Mo</span><span class="weekday">Tu</span><span class="weekday">We</span><span class="weekday">Th</span><span class="weekday">Fr</span><span class="weekday">Sa</span><span class="weekday">Su</span>
    <span class="day outside">31</span><span class="day">1</span><span class="day">2</span><span class="day">3</span><span class="day">4</span><span class="day weekend">5</span><span class="day weekend">6</span>
    <span class="day">7</span><span class="day">8</span><span class="day">9</span><span class="day">10</span><span class="day">11</span><span class="day weekend">12</span><span class="day weekend">13</span>
    <span class="day">14</span><span class="day">15</span><span class="day">16</span><span class="day">17</span><span class="day">18</span><span class="day weekend">19</span><span class="day weekend">20</span>
    <span class="day">21</span><span class="day">22</span><span class="day">23</span><span class="day">24</span><span class="day">25</span><span class="day weekend">26</span><span class="day weekend">27</span>
    <span class="day">28</span><span class="day">29</span><span class="day">30</span><span class="day outside">1</span><span class="day outside">2</span><span class="day outside">3</span><span class="day outside">4</span>
  </div>
</section>

<section class="month-page month-page--oct">
  <h2 class="month-title">October 2015</h2>
  <div class="photo-collage">
    <div class="tile tile--main" role="img" aria-label="Photo slot: baby sitting in a cot with a plush toy"></div>
    <div class="tile tile--top" role="img" aria-label="Photo slot: close-up of smiling baby"></div>
    <div class="tile tile--bottom" role="img" aria-label="Photo slot: baby on a sofa holding a football"></div>
  </div>
  <div class="date-grid">
    <span class="weekday">Mo</span><span class="weekday">Tu</span><span class="weekday">We</span><span class="weekday">Th</span><span class="weekday">Fr</span><span class="weekday">Sa</span><span class="weekday">Su</span>
    <span class="day outside">28</span><span class="day outside">29</span><span class="day outside">30</span><span class="day">1</span><span class="day">2</span><span class="day weekend">3</span><span class="day weekend">4</span>
    <span class="day">5</span><span class="day">6</span><span class="day">7</span><span class="day">8</span><span class="day">9</span><span class="day weekend">10</span><span class="day weekend">11</span>
    <span class="day">12</span><span class="day">13</span><span class="day">14</span><span class="day">15</span><span class="day">16</span><span class="day weekend">17</span><span class="day weekend">18</span>
    <span class="day">19</span><span class="day">20</span><span class="day">21</span><span class="day">22</span><span class="day">23</span><span class="day weekend">24</span><span class="day weekend">25</span>
    <span class="day">26</span><span class="day">27</span><span class="day">28</span><span class="day">29</span><span class="day">30</span><span class="day weekend">31</span><span class="day outside">1</span>
  </div>
</section>

<section class="month-page month-page--nov">
  <h2 class="month-title">November 2015</h2>
  <div class="photo-slot photo-slot--nov" role="img" aria-label="Photo slot: baby in a blue sun hat in the garden"></div>
  <div class="date-grid">
    <span class="weekday">Mo</span><span class="weekday">Tu</span><span class="weekday">We</span><span class="weekday">Th</span><span class="weekday">Fr</span><span class="weekday">Sa</span><span class="weekday">Su</span>
    <span class="day outside">26</span><span class="day outside">27</span><span class="day outside">28</span><span class="day outside">29</span><span class="day outside">30</span><span class="day outside">31</span><span class="day weekend">1</span>
    <span class="day">2</span><span class="day">3</span><span class="day">4</span><span class="day">5</span><span class="day">6</span><span class="day weekend">7</span><span class="day weekend">8</span>
    <span class="day">9</span><span class="day">10</span><span class="day">11</span><span class="day">12</span><span class="day">13</span><span class="day weekend">14</span><span class="day weekend">15</span>
    <span class="day">16</span><span class="day">17</span><span class="day">18</span><span class="day">19</span><span class="day">20</span><span class="day weekend">21</span><span class="day weekend">22</span>
    <span class="day">23</span><span class="day">24</span><span class="day">25</span><span class="day">26</span><span class="day">27</span><span class="day weekend">28</span><span class="day weekend">29</span>
    <span class="day">30</span><span class="day outside">1</span><span class="day outside">2</span><span class="day outside">3</span><span class="day outside">4</span><span class="day outside">5</span><span class="day outside">6</span>
  </div>
</section>

<section class="month-page month-page--dec">
  <h2 class="month-title">December 2015</h2>
  <div class="photo-slot photo-slot--dec" role="img" aria-label="Photo slot: laughing baby on a wooden rocking horse by the Christmas tree"></div>
  <div class="date-grid">
    <span class="weekday">Mo</span><span class="weekday">Tu</span><span class="weekday">We</span><span class="weekday">Th</span><span class="weekday">Fr</span><span class="weekday">Sa</span><span class="weekday">Su</span>
    <span class="day outside">30</span><span class="day">1</span><span class="day">2</span><span class="day">3</span><span class="day">4</span><span class="day weekend">5</span><span class="day weekend">6</span>
    <span class="day">7</span><span class="day">8</span><span class="day">9</span><span class="day">10</span><span class="day">11</span><span class="day weekend">12</span><span class="day weekend">13</span>
    <span class="day">14</span><span class="day">15</span><span class="day">16</span><span class="day">17</span><span class="day">18</span><span class="day weekend">19</span><span class="day weekend">20</span>
    <span class="day">21</span><span class="day">22</span><span class="day">23</span><span class="day">24</span><span class="day">25</span><span class="day weekend">26</span><span class="day weekend">27</span>
    <span class="day">28</span><span class="day">29</span><span class="day">30</span><span class="day">31</span><span class="day outside">1</span><span class="day outside">2</span><span class="day outside">3</span>
  </div>
</section>

</body>
</html>
```